Stage Design Company Business Card

We are looking to step up up our business card design for our team.

We are a Full service Design and Consultation company for Stage and TV with an emphasis in Theatrical Lighting.

We like our materials to be clean and modern with solid colors free of patterns and gradients. Our brand consists of 4 primary colors Purple, Black, Grey, and White. Provided is our Word Mark as well as our Symbol Logo.

We would like our cards to leave an impression beyond the information, show our attention to design and detail, and make our marks an easily recognized feature (together or apart) for our clients.

We need a warm approachable comfortable feel for some clients, and a professional flair for the board member type clients.

Attached are our brand elements, and our existing cards to give a sense of our style and a glipse at the information we provide on our cards.

Target Market(s)

broad client base from church leaders to high school teachers and architects.

Industry/Entity Type

Business

Contact Information for Business Card

We format our phone number with periods not parenthesis or dashes. Information will be edited for each of our team members, and team member specific cards are not part of this scope, but rather a template so to speak.

Font styles to use
Sans Serif

Colors
6b449b
ffffff
000000
333333
aaaaaa

Requirements
Must have
• Wordmark and logo mark present (does not need to exist on the same side of card)
• Brand Colors,
• Name, Phone, Email, Address.
• Unique choices that make someone stop and take a second look
Nice to have
• It would be nice to somehow convey what we DO, as our brand name does not lend itself to this, outside of an obvious tagline though.....
• social media if not crowded. all of our handles match (instagram, twitter, facebook)
Should not have
• "clipart"

```html
<!DOCTYPE html>
<html lang="en">
<head>
<meta charset="utf-8">
<title>Marlow Entertainment – Business Card</title>
<link rel="stylesheet" href="https://fonts.googleapis.com/css2?family=Questrial&display=swap">
<style>
  :root {
    --stage: #2b2b2b;
    --card-purple: #3b2670;
    --ink-white: #ffffff;
    --rule-white: rgba(255,255,255,0.85);
    --muted-white: rgba(255,255,255,0.7);
  }
  * { box-sizing: border-box; margin: 0; padding: 0; }
  html, body {
    width: 1200px; height: 880px; overflow: hidden;
    background: var(--stage);
    font-family: "Questrial", sans-serif;
    color: var(--ink-white);
  }
  .canvas { position: relative; width: 1200px; height: 880px; }

  .card {
    position: absolute;
    width: 560px; height: 320px;
    background: var(--card-purple);
    border-radius: 22px;
    overflow: hidden;
  }
  .card--front { left: 90px; top: 110px; }
  .card--back  { left: 550px; top: 450px; }

  /* Front */
  .brand {
    position: absolute; inset: 0;
    display: flex; flex-direction: column;
    align-items: center; justify-content: center;
  }
  .brand__dot {
    width: 54px; height: 54px; border-radius: 50%;
    border: 5px solid var(--ink-white);
    margin-bottom: 26px;
  }
  .brand__name {
    font-size: 34px; letter-spacing: 0.42em;
    padding-left: 0.42em; line-height: 1;
  }
  .brand__tagline {
    margin-top: 14px; font-size: 9px;
    letter-spacing: 0.9em; padding-left: 0.9em;
    color: var(--muted-white);
  }

  /* Back */
  .back-accent {
    position: absolute; left: -120px; bottom: -170px;
    width: 380px; height: 380px;
  }
  .contact {
    position: absolute; right: 34px; top: 52px;
    width: 270px; text-align: center;
  }
  .contact__name { font-size: 27px; letter-spacing: 0.06em; }
  .contact__rule {
    border: 0; border-top: 2px dotted var(--rule-white);
    margin: 10px 0 12px;
  }
  .contact__line { font-size: 19px; line-height: 1.45; }
  .contact__line--phone { font-size: 22px; letter-spacing: 0.03em; }
  .contact__address { font-size: 18px; line-height: 1.35; letter-spacing: 0.04em; }
</style>
</head>
<body>
<main class="canvas">

  <section class="card card--front" aria-label="Card front">
    <div class="brand">
      <span class="brand__dot" aria-hidden="true"></span>
      <div class="brand__name">MARLOW</div>
      <div class="brand__tagline">ENTERTAINMENT</div>
    </div>
  </section>

  <section class="card card--back" aria-label="Card back">
    <svg class="back-accent" viewBox="0 0 380 380" aria-hidden="true">
      <circle cx="190" cy="190" r="170" fill="none" stroke="#ffffff" stroke-width="22"/>
    </svg>
    <div class="contact">
      <div class="contact__name">TOM R MARLOW</div>
      <hr class="contact__rule">
      <div class="contact__line contact__line--phone">555.014.7381</div>
      <div class="contact__line">tom@marlow-e.com</div>
      <hr class="contact__rule">
      <div class="contact__address">18 N OAK ST<br>FAIRVIEW, AZ 85999</div>
    </div>
  </section>

</main>
</body>
</html>
```